4 Information One pagers needed for Australia's biggest Oil & Gas Conference

KVR is a global organisation with its corporate headquarters located in Perth, Western Australia and regional offices in Brisbane, Darwin, Singapore, Korea & China.
KVR delivers dedicated project support services, incorporating but not limited to; project design, procurement, construction, installation, commissioning, operations and maintenance. Our cross industry expertise, project expertise and track record of successfully delivering international projects with blue chip clients and partners has led to our fast evolving reputation as a preferred supplier worldwide within the oil and gas industry onshore and offshore within both greenfield and brownfield scopes.

Need to get information on a one page handout. There are 4 documents that need to be developed.

We need a banner across the top and bottom of each page, which has our logo, title of the document, and our contact details (Head Office – Address: Unit 17, 46-48 Marlow Lane, Perth WA 6000 Australia. Phone: +61 8 9371 5086) Needs to keep with the KVR colours but use images that are relevant to the oil and gas/commissioning industries. Our previous “who we are” flyer is attached so you have a feel for what we are after.

Page 1: KVR’ service offerings include (for each take brief paragraph from document attached for description of each. If unable to find information please contact us or search on www.brenvatek.com):
• Engineering Design;
• Construction Management;
• Commissioning (Systems, Processes, Resources);
• Completions Strategy;
• Multi-Disciplinary Engineering;
• Multi-Disciplinary Technicians;
• Operations & Maintenance Support;
• EX Inspect & Maintain;
• On Site Nitrogen Production;
• Water Treatment;
• Compact Separation Systems;
• Processes to support services;
o Technology to improve efficiency and productivity (Finishline Relay, TW Relay).

Page 2: Our Team – please complete in order listed below and images are attached
Derek Halvorsen
Chief Executive Officer (CEO)
An extensively experienced and practical executive in the engineering industry with over 20 years’ service, more specifically in the oil and gas sector, since 1988.
The experience has been gained through a wide array of projects throughout Australia and Overseas working in the area of Design, System Analysing, Commissioning and Construction before commencing in Business Development and then finally Company Management and Directorships.
Derek has gained extensive experience in line and project management roles and more particularly in change management, people development and team motivation.
He has extensive experience leading and working in teams associated with design, construction and commissioning of world scale capital projects in both ‘brownfields’ and ‘Greenfields’ scenarios.
Simon Whitlock
Chief Financial Officer
Simon is a qualified accountant (CGMA, CMA, CPA. MAAT) and brings to the team over 20 years of Australian and International experience in a number of key financial roles at both SXA listed and private companies. Simon comes to the team with a strong financial, commercial and business analytical skills combined with proven effective leadership of finance teams. Simon has significant experience in managing working capital requirements of growth businesses with an international footprint. Simon is a member of Southern Guild of Registered Ledger Keepers, Royal College of Business Bookkeepers & Federation of Ledger Practitioners.

Clara Venditti
HR Manager
Clara has more than 10 years’ experience across Oil & Gas, Resources, Engineering, and Finance industries. With general human resources experience, Clara has led strategic and operational HR support and services across recruitment, on boarding, training, remuneration and benefits, employment contract management, career planning and organisational accreditation for 457 visas. Further to this Clara has also managed HR within the M & A environment, through due diligence and post-acquisition integration on both buy and sell sides within the context of global organisations.

Gregory Lane
Project Services & Agency Representative
Project Services and Management expertise with local and international experience in the oil & gas, mining, and utilities industries, as well as a strong understanding within the finance sector. Andrew’s strengths and experience lie in developing and executing business proposals, as well as liaising with external consultants and clients. Possessing competent financial and economic modelling skills and the ability to utilise data for risk and profit based outcomes. Andrew has managed ISO 9001 implementation and ensures that all quality assurance processes are adhered to.
Andrew holds both Bachelor of Commerce and Master of Commerce (Economics & Finance) degrees and is working towards a Master of Science (Energy).

Martin Dunleavy
Director: KVR NT
Andrew has lived in the North of Australia for the last 26 years, bringing valuable local knowledge to the KVR NT office. He has owned and operated his NT services business for 17 years; servicing local and international clients before concentrating and moving into the Oil & Gas and Mining Sector. Andrew has many years of experience in logistics, service and supply, his extensive experience in the NT comes from the following industries: Oil & Gas; Mining; Exploration; Pastoral, Commercial Marine; and Construction.

Trevor Hanlon
Business Development Manager- Queensland
Trevor is a professional civil and mechanical engineer with more than 40 years’ experience in Australia and internationally, across consulting, construction and manufacturing sectors at operational and executive levels. He has held a number of senior executive roles with companies including Rendle Valve Systems, KTV Varnor, and Coastline Transit and has served on a number of industry associations, government committees and private sector boards.

Trevor has broad knowledge and experience in Australian and international business, with an extensive professional network throughout Australia, Asia, Europe and the United States. He has manufactured and supplied products to the oil and gas, petrochemical, power, water, military and nuclear industries.

Page 3: Our Influence
We need the headlines and logos of the following articles and publications:
https://www.tradewirejournal.com.au/article/KVR-buys-Singapore-recruitment-firm?sthash_Q7HkRmWp_tzbe=
http://www.fuelreportdaily.net/storyview.asp?storyID=512847391§ion=Careers+%26+Recruitment§ionsource=s318&aspdsc=yes#.KpdRwtH83MZ.linkedin
http://www.fuelreportdaily.net/storyview.asp?storyID=512847652§ion=Industry+Moves§ionsource=s91&Highlight=kvr&aspdsc=yes
Southern Crude & Fuel Review – this one is getting published soon so just the logo for this one at this time?

Page 4: Who we work with?
Need to have just all logos of the companies that we have worked with. Attached is logos of our clients to match the list below. May need to find better resolution ones.
- Voltrax
- Condor Energy
- Veranta Global
- Fernholt
- PBW – Pelican Boring Worldwide
- Moventa
- Starke Petrol
- Hanbit Fuel Development Company
- Crest
- TQ Group
- LW
- Zephra Rotors
- Orrin Petroleum
- Keta Energy
- Brackwell Alloys Group (BAG)
- Pinnacle Energy
- Tirolo Resources
- Millbrook Meats
- Dorvan
- Hartigan Ledger
- Veshar South Korea
- Kelt Ridge Iron Ore
- Worldwide Utility Holdings
- Falcon Oil
- Tandrel
- Brundle Nickel
- Vintro Oil
- Durvane
- KMT
- Thornbury Alumina

• DIN Offc

• 4 separate pages:
• 1. Menu of Services
• 2. Our Team
• 3. Our Influences (media companies)
• 4. Who we work with
• Keep in colours of KVR and ensure same header/footer used for all 4 pages
• orange = #D76927, R-215 G-105 B-39, CMYK C-11.65 M-70.4 Y-100 K-1.52
• Blue = #21224B, R-33 G-34 B-75, CMYK C-95.65, M-92.65 Y-39.82, K40.01
• Same theme across all 4
• Visually appealing
• Brief information
• Colour
• Images
• Made up information - if unsure please contact us

```html
<!DOCTYPE html>
<html lang="en">
<head>
<meta charset="utf-8">
<title>KVR – Our Team</title>
<link href="https://fonts.googleapis.com/css2?family=Source+Sans+3:wght@400;600;700&display=swap" rel="stylesheet">
<style>
:root{
  --orange:#D76927;
  --navy:#21224B;
  --white:#ffffff;
  --ink:#1d1d1d;
  --sky-a:#9fc4e6;
  --sky-b:#2f78b9;
  --photo-bg:#c9d2dc;
}
*{box-sizing:border-box;margin:0;padding:0}
html,body{width:860px;height:1200px;overflow:hidden;background:var(--white)}
body{font-family:"Source Sans 3",Arial,sans-serif;color:var(--ink)}
.sheet{position:relative;width:860px;height:1200px;overflow:hidden;background:var(--white)}
.bar{position:absolute;left:0;width:860px;background:var(--orange);color:var(--white);font-weight:600;font-size:16px;z-index:5}
.bar-top{top:0;height:42px;display:flex;align-items:center;justify-content:space-between;padding:0 36px 0 26px}
.bar-bottom{top:1140px;height:60px}
.bar-bottom .contact{position:absolute;right:14px;top:6px;text-align:right;line-height:24px}
.bar-bottom .brand-tile{position:absolute;left:0;top:0;width:196px;height:60px;background:var(--white)}
.brand{display:flex;align-items:center;gap:10px;font-weight:700;color:var(--navy)}
.brand-mark{width:20px;height:20px;border-radius:50%;background:var(--orange)}
.brand-top{position:absolute;left:312px;top:58px;height:66px;font-size:48px;letter-spacing:2px}
.brand-bottom{position:absolute;left:34px;top:4px;font-size:42px;letter-spacing:2px}
.page-title{position:absolute;left:670px;top:66px;font-size:32px;font-weight:600;color:var(--orange)}
.panel{position:absolute;background:var(--navy)}
.panel-left{left:0;top:55px;width:290px;height:1085px}
.panel-right{left:562px;top:130px;width:298px;height:1010px}
.photo{position:absolute;background:linear-gradient(135deg,var(--sky-a),var(--sky-b) 55%,#17406f)}
.photo-plain{background:linear-gradient(180deg,#dfe4ea,var(--photo-bg))}
.member{position:absolute}
.member h2{font-size:28px;font-weight:600;text-align:center;line-height:30px}
.member h3{font-size:19px;font-weight:600;text-align:center;line-height:23px}
.member p{font-size:11px;line-height:19.5px;text-align:justify}
.member p.indent{text-indent:38px}
.on-navy{color:var(--white)}
.on-white{color:var(--ink)}
</style>
</head>
<body>
<main class="sheet">
  <header class="bar bar-top">
    <span>Head Office – Address: Unit 17, 46-48 Marlow Lane, Perth WA 6000 Australia.</span>
    <span>Phone: +61 8 9371 5086</span>
  </header>

  <div class="panel panel-left"></div>
  <div class="panel panel-right"></div>

  <div class="brand brand-top"><span class="brand-mark"></span>KVR</div>
  <h1 class="page-title">Our Team</h1>

  <div class="photo" style="left:0;top:55px;width:290px;height:180px" role="img" aria-label="Portrait of Derek Halvorsen, Chief Executive Officer, against a blue background"></div>
  <section class="member on-navy" style="left:12px;top:240px;width:268px">
    <h2>Derek Halvorsen</h2>
    <h3>Chief Executive Officer (CEO)</h3>
    <p class="indent" style="margin-top:9px">An extensively experienced and practical executive in the engineering industry with over 20 years’ service, more specifically in the oil and gas sector, since 1988. The experience has been gained through a wide array of projects throughout Australia and Overseas working in the area of Design, System Analysing, Commissioning and Construction before commencing in Business Development and then finally Company Management and Directorships.</p>
    <p class="indent">Derek has gained extensive experience in line and project management roles and more particularly in change management, people development and team motivation. He has extensive experience leading and working in teams associated with design, construction and commissioning of world scale capital projects in both ‘brownfields’ and ‘Greenfields’ scenarios.</p>
  </section>

  <div class="photo" style="left:290px;top:135px;width:272px;height:190px" role="img" aria-label="Portrait of Clara Venditti, HR Manager, against a blue background"></div>
  <section class="member on-white" style="left:297px;top:326px;width:258px">
    <h2>Clara Venditti</h2>
    <h3>HR Manager</h3>
    <p class="indent" style="margin-top:4px">Clara has more than 10 years’ experience across Oil &amp; Gas, Resources, Engineering, and Finance industries. With general human resources experience, Clara has led strategic and operational HR support and services across recruitment, on boarding, training, remuneration and benefits, employment contract management, career planning and organisational accreditation for 457 visas. Further to this Clara has also managed HR within the M &amp; A environment, through due diligence and post-acquisition integration on both buy and sell sides within the context of global organisations.</p>
  </section>

  <div class="photo photo-plain" style="left:600px;top:138px;width:195px;height:187px" role="img" aria-label="Portrait of Martin Dunleavy, Director of KVR NT"></div>
  <section class="member on-navy" style="left:571px;top:324px;width:280px">
    <h2>Martin Dunleavy</h2>
    <h3>Director: KVR NT</h3>
    <p>Martin has lived in the North of Australia for the last 26 years, bringing valuable local knowledge to the KVR NT office. He has owned and operated his NT services business for 17 years; servicing local and international clients before concentrating and moving into the Oil &amp; Gas and Mining Sector. Martin has many years of experience in logistics, service and supply, his extensive experience in the NT comes from the following industries: Oil &amp; Gas; Mining; Exploration; Pastoral, Commercial Marine; and Construction.</p>
  </section>

  <div class="photo" style="left:0;top:630px;width:290px;height:140px" role="img" aria-label="Portrait of Simon Whitlock, Chief Financial Officer, against a blue background"></div>
  <section class="member on-navy" style="left:12px;top:802px;width:268px">
    <h2>Simon Whitlock</h2>
    <h3>Chief Financial Officer</h3>
    <p class="indent" style="margin-top:24px">Simon is a qualified accountant (CGMA, CMA, CPA. MAAT) and brings to the team over 20 years of Australian and International experience in a number of key financial roles at both SXA listed and private companies. Simon comes to the team with a strong financial, commercial and business analytical skills combined with proven effective leadership of finance teams. Simon has significant experience in managing working capital requirements of growth businesses with an international footprint. Simon is a member of Southern Guild of Registered Ledger Keepers, Royal College of Business Bookkeepers &amp; Federation of Ledger Practitioners.</p>
  </section>

  <div class="photo" style="left:297px;top:630px;width:257px;height:150px" role="img" aria-label="Portrait of Gregory Lane, Project Services and Agency Representative, against a blue background"></div>
  <section class="member on-white" style="left:297px;top:778px;width:258px">
    <h2>Gregory Lane</h2>
    <h3>Project Services &amp; Agency Representative</h3>
    <p style="margin-top:6px">Project Services and Management expertise with local and international experience in the oil &amp; gas, mining, and utilities industries, as well as a strong understanding within the finance sector. Gregory’s strengths and experience lie in developing and executing business proposals, as well as liaising with external consultants and clients. Possessing competent financial and economic modelling skills and the ability to utilise data for risk and profit based outcomes. Gregory has managed ISO 9001 implementation and ensures that all quality assurance processes are adhered to. Gregory holds both Bachelor of Commerce and Master of Commerce (Economics &amp; Finance) degrees and is working towards a Master of Science (Energy).</p>
  </section>

  <div class="photo photo-plain" style="left:595px;top:565px;width:202px;height:200px" role="img" aria-label="Portrait of Trevor Hanlon, Business Development Manager Queensland"></div>
  <section class="member on-navy" style="left:571px;top:770px;width:280px">
    <h2>Trevor Hanlon</h2>
    <h3>Business Development Manager- Queensland</h3>
    <p class="indent" style="margin-top:6px">Trevor is a professional civil and mechanical engineer with more than 40 years’ experience in Australia and internationally, across consulting, construction and manufacturing sectors at operational and executive levels. He has held a number of senior executive roles with companies including Rendle Valve Systems, KTV Varnor, and Coastline Transit and has served on a number of industry associations, government committees and private sector boards.</p>
    <p class="indent">Trevor has broad knowledge and experience in Australian and international business, with an extensive professional network throughout Australia, Asia, Europe and the United States. He has manufactured and supplied products to the oil and gas, petrochemical, power, water, military and nuclear industries.</p>
  </section>

  <footer class="bar bar-bottom">
    <div class="brand-tile"><div class="brand brand-bottom"><span class="brand-mark"></span>KVR</div></div>
    <div class="contact">Head Office – Address: Unit 17, 46-48 Marlow Lane, Perth WA 6000 Australia.<br>Phone: +61 8 9371 5086</div>
  </footer>
</main>
</body>
</html>
```